Veltrane New Business Card Design IT Company

PLEASE CHECK ATTACHED PDF DOC FOR DETAILS. I have put exactly what I want to save time and finish the project asap thanks.

Veltrane Consulting is an Information Management Consulting company providing IT Professional Services Consulting services to both Public and private sector.
Need a Business Card Design to represent. It has to be Premium Raised Spot Glass finish.
Company Name: Veltrane Consulting
Company Website: veltrane-example.com.au
Company Slogan: Precise Thinking, Reliable Delivery
Name on Card: Lor Bemis
Title: Managing Partner
Email: Lor.Bemis@veltrane-example.com.au
Phone: 0400000000

Company Logo is under construction from SketchHive
Company Logo & Company Name Font Color should Match and have to Electric Aqua Blue
Company Logo at the Back Side of the Card
Card Background color preference: Slight Grey or Black to make the logo and company Name stand Out.

Any Questions please Ask.

Industry/Entity Type

Construction

Contact Information for Business Card

PLEASE CHECK ATTACHED PDF DOC FOR DETAILS. I have put exactly what I want to save time and finish the project asap thanks
Name on Card: Lor Bemis
Title: Managing Partner
Phone: 0400000000

Requirements
Must have
• PLEASE CHECK ATTACHED PDF DOC FOR DETAILS. I have put exactly what I want to save time and finish the project asap thanks
• Company Logo, Company Name, Company website Company Slogan at the back side of the Card with custom dark blue front and back background
• Company Logo, Company Name , Company Website at the Front of the Card Title and Name email and phone in the front also in white color font
Should not have
• Should not Have Decorative or Script Fonts
• Its a IT company so must be professional no flowers or waterfalls etc

```html
<!DOCTYPE html>
<html lang="en">
<head>
<meta charset="utf-8">
<title>Veltrane Consulting Business Cards</title>
<link rel="stylesheet" href="https://fonts.googleapis.com/css2?family=Montserrat:wght@600;700&family=Questrial&display=swap">
<style>
  :root {
    --stage-light: #8fd6e8;
    --stage-mid: #3ab3cf;
    --stage-dark: #1c94b2;
    --card-core: #12325a;
    --card-edge: #07142a;
    --aqua: #2aa7e6;
    --aqua-deep: #0f6fc0;
    --ink: #101c38;
    --white: #ffffff;
    --paper: #ffffff;
  }
  * { box-sizing: border-box; margin: 0; padding: 0; }
  html, body { width: 698px; height: 1200px; overflow: hidden; }
  body {
    position: relative;
    background: radial-gradient(ellipse 90% 70% at 20% 5%, var(--stage-light) 0%, var(--stage-mid) 45%, var(--stage-dark) 100%);
    font-family: "Questrial", Arial, sans-serif;
  }
  .card {
    position: absolute;
    left: 88px;
    width: 524px;
    border-radius: 18px;
    overflow: hidden;
    background: radial-gradient(ellipse 70% 75% at 50% 45%, var(--card-core) 0%, var(--card-edge) 100%);
    box-shadow: 0 6px 14px rgba(0, 20, 40, 0.45);
  }
  .card--front { top: 102px; height: 294px; }
  .card--slogan { top: 446px; height: 293px; }
  .card--brand { top: 792px; height: 294px; }

  .wordmark {
    font-family: "Montserrat", Arial, sans-serif;
    font-weight: 700;
    color: var(--aqua);
    white-space: nowrap;
  }
  .mark-dot {
    display: inline-block;
    border-radius: 50%;
    background: var(--aqua);
  }

  /* front */
  .front-brand {
    position: absolute; top: 44px; left: 0; right: 0;
    display: flex; justify-content: center; align-items: center; gap: 12px;
  }
  .front-brand .mark-dot { width: 34px; height: 34px; }
  .front-brand .wordmark { font-size: 28px; }
  .front-wave { position: absolute; left: 0; top: 0; width: 524px; height: 294px; }
  .holder { position: absolute; left: 40px; top: 212px; color: var(--ink); }
  .holder-name { font-family: "Montserrat", Arial, sans-serif; font-weight: 700; font-size: 31px; line-height: 1; }
  .holder-title { font-size: 13px; margin-top: 6px; }
  .contacts { position: absolute; left: 246px; top: 204px; list-style: none; color: var(--ink); }
  .contacts li { display: flex; align-items: center; height: 22px; font-size: 14px; white-space: nowrap; }
  .contacts svg { width: 12px; height: 12px; flex: none; }
  .contacts .sep { width: 1px; height: 14px; background: var(--ink); margin: 0 8px 0 6px; }

  /* back cards */
  .centre-stack {
    position: absolute; left: 0; right: 0;
    display: flex; flex-direction: column; align-items: center; text-align: center;
  }
  .card--slogan .centre-stack { top: 36px; }
  .card--brand .centre-stack { top: 36px; }
  .centre-stack .mark-dot { width: 84px; height: 84px; margin-bottom: 20px; }
  .card--slogan .wordmark { font-size: 48px; line-height: 1; }
  .slogan { color: var(--white); font-size: 17.5px; margin-top: 22px; }
  .site { color: var(--white); font-size: 18px; margin-top: 20px; }
  .card--brand .wordmark { font-size: 42px; line-height: 1.08; }
</style>
</head>
<body>

  <section class="card card--front">
    <svg class="front-wave" viewBox="0 0 524 294" aria-hidden="true">
      <defs>
        <linearGradient id="band" x1="0" x2="1" y1="0" y2="0">
          <stop offset="0" stop-color="#1a8fe0"/>
          <stop offset="0.5" stop-color="#2aa7e6"/>
          <stop offset="1" stop-color="#0f6fc0"/>
        </linearGradient>
      </defs>
      <path d="M0,120 C140,92 290,150 410,172 C460,181 500,180 524,174 L524,294 L0,294 Z" fill="url(#band)"/>
      <path d="M0,150 C120,118 260,150 370,176 C440,192 495,196 524,192 L524,294 L0,294 Z" fill="var(--paper)"/>
    </svg>
    <div class="front-brand">
      <span class="mark-dot"></span>
      <span class="wordmark">Veltrane Consulting</span>
    </div>
    <div class="holder">
      <p class="holder-name">Lor Bemis</p>
      <p class="holder-title">Managing Partner</p>
    </div>
    <ul class="contacts">
      <li>
        <svg viewBox="0 0 12 12"><rect x="3" y="0.5" width="6" height="11" rx="1.2" fill="none" stroke="#101c38"/><circle cx="6" cy="9.6" r="0.7" fill="#101c38"/></svg>
        <span class="sep"></span>0400 000 000
      </li>
      <li>
        <svg viewBox="0 0 12 12"><rect x="1" y="3" width="10" height="7" rx="1" fill="#101c38"/><path d="M1.5,3.5 L6,7 L10.5,3.5" fill="none" stroke="#fff" stroke-width="0.9"/></svg>
        <span class="sep"></span>lor.bemis@veltrane-example.com.au
      </li>
      <li>
        <svg viewBox="0 0 12 12"><circle cx="6" cy="6" r="5" fill="none" stroke="#101c38" stroke-width="1.2"/><path d="M1,6 H11 M6,1 C3.5,4 3.5,8 6,11 C8.5,8 8.5,4 6,1" fill="none" stroke="#101c38" stroke-width="0.9"/></svg>
        <span class="sep"></span>veltrane-example.com.au
      </li>
    </ul>
  </section>

  <section class="card card--slogan">
    <div class="centre-stack">
      <span class="mark-dot"></span>
      <span class="wordmark">Veltrane</span>
      <p class="slogan">Precise Thinking, Reliable Delivery</p>
      <p class="site">veltrane-example.com.au</p>
    </div>
  </section>

  <section class="card card--brand">
    <div class="centre-stack">
      <span class="mark-dot"></span>
      <span class="wordmark">Veltrane<br>Consulting</span>
    </div>
  </section>

</body>
</html>
```